Stationary and design update for my brand

I need new letterhead, a new business card, business envelope design, new keynote and powerpoint branded slides (16x9). I have logo samples in various styles and brand standards for fonts and colors.

Font styles to use
Sans Serif

```html
<!DOCTYPE html>
<html lang="en">
<head>
<meta charset="utf-8">
<title>Brightwell Envelope Set</title>
<link href="https://fonts.googleapis.com/css2?family=Montserrat:wght@400;600;700&display=swap" rel="stylesheet">
<style>
  :root {
    --bg: #ececec;
    --paper: #f6f6f6;
    --brand-orange: #d4862e;
    --soft-tan: #ecdcc8;
    --ink: #555555;
    --edge: #dedede;
  }
  * { margin: 0; padding: 0; box-sizing: border-box; }
  html, body {
    width: 1200px;
    height: 795px;
    overflow: hidden;
    background: var(--bg);
    font-family: "Montserrat", sans-serif;
  }
  .canvas {
    position: relative;
    width: 1200px;
    height: 795px;
  }
  .envelope {
    position: absolute;
    width: 560px;
    height: 260px;
    background: var(--paper);
    border: 1px solid var(--edge);
    border-radius: 3px;
    box-shadow: 0 10px 24px rgba(0,0,0,0.10);
    overflow: hidden;
  }
  .envelope--back { left: 590px; top: 100px; }
  .envelope__flap {
    position: absolute;
    left: 0; top: 0;
    width: 100%;
    height: 112px;
    background: var(--brand-orange);
    border-bottom-left-radius: 6px;
    border-bottom-right-radius: 6px;
    display: flex;
    align-items: center;
    justify-content: center;
  }
  .wordmark {
    font-weight: 700;
    letter-spacing: 2px;
    line-height: 1;
  }
  .wordmark--light { color: #ffffff; font-size: 24px; }
  .return-address {
    position: absolute;
    left: 140px;
    top: 150px;
    color: var(--ink);
    font-size: 13px;
    line-height: 1.5;
    font-style: normal;
  }
  .return-address__name { font-weight: 700; }
  .return-address__street { font-weight: 400; }

  .envelope--front { left: 60px; top: 400px; }
  .envelope__brand {
    position: absolute;
    left: 28px;
    top: 26px;
  }
  .wordmark--accent { color: var(--brand-orange); font-size: 22px; }
  .envelope__decor {
    position: absolute;
    left: 0;
    bottom: 0;
    width: 100%;
    height: 150px;
    background: linear-gradient(180deg, rgba(236,220,200,0) 0%, rgba(236,220,200,0.55) 100%);
  }
</style>
</head>
<body>
  <main class="canvas">
    <section class="envelope envelope--back" aria-label="Envelope back">
      <div class="envelope__flap">
        <span class="wordmark wordmark--light">BRIGHTWELL</span>
      </div>
      <address class="return-address">
        <div class="return-address__name">Brightwell Learning and Growth Partners LLC</div>
        <div class="return-address__street">207 Maple Grove Rd. Ashford, OR 97520</div>
      </address>
    </section>

    <section class="envelope envelope--front" aria-label="Envelope front">
      <div class="envelope__brand">
        <span class="wordmark wordmark--accent">BRIGHTWELL</span>
      </div>
      <div class="envelope__decor" role="img" aria-label="Faint tan brand decoration across the lower envelope"></div>
    </section>
  </main>
</body>
</html>
```